Quarveling stickers design for our main topics (for example: agile and Kanban)

We are looking for sticker design, that will reflect our cooperate identity and can be used for the different topics in our company. We would like to start with our Agile Coaching Offers with a Kanban Sticker saying "stop starting, start finishing", A bad example can be find in the file upload ;)
Check out our homepage to get a feeling for the cooperate identity (www.quarveling.ch)

Target Market(s)

Customers and trainees from our trainings

Industry/Entity Type

Consulting

Colors
0355a3
fbed22

Requirements
Must have
• a cool design thats fits to our customer design
the 2 lines can be changed for future stickers ... like in the example "stop starting, start finishing" and "we show you how"
Nice to have
• -
Should not have
• -

```html
<!DOCTYPE html>
<html lang="en">
<head>
<meta charset="utf-8">
<title>Quarveling Kanban Stickers</title>
<link href="https://fonts.googleapis.com/css2?family=Arimo:ital,wght@0,400;1,400;1,700&display=swap" rel="stylesheet">
<style>
  :root {
    --bg-light: #fbfbfb;
    --bg-mid: #e4e4e4;
    --brand-blue-top: #0336ea;
    --brand-blue-bottom: #1c3aa3;
    --link-blue: #0a33d6;
    --panel-white: #ffffff;
    --panel-grey: #dcdcde;
    --note-yellow-top: #f1f28a;
    --note-yellow-bottom: #fbfb9c;
    --ink: #111111;
    --logo-blue: #0a3be0;
  }
  * { margin: 0; padding: 0; box-sizing: border-box; }
  html, body { width: 1200px; height: 1000px; overflow: hidden; }
  body {
    position: relative;
    font-family: "Arimo", Arial, sans-serif;
    background: linear-gradient(180deg, var(--bg-light) 0%, var(--bg-mid) 50%, var(--bg-light) 100%);
  }
  .sticker { position: absolute; left: 205px; width: 811px; height: 206px; }
  .sticker--top { top: 270px; }
  .sticker--bottom { top: 517px; height: 205px; }

  .sticker__base {
    position: absolute; inset: 0;
    background: linear-gradient(180deg, #f3f3f4 0%, var(--panel-grey) 100%);
    box-shadow: 0 3px 6px rgba(0,0,0,0.18);
  }
  .sticker--top .sticker__base { border-radius: 60px 4px 66px 0; border: 2px solid #fff; }
  .sticker--bottom .sticker__base { border-radius: 70px 4px 66px 0; }

  .band { position: absolute; }
  .band--headline {
    background: linear-gradient(180deg, var(--brand-blue-top) 0%, var(--brand-blue-bottom) 100%);
    color: #fff;
    font-size: 40px;
    font-style: italic;
    display: flex; align-items: center;
    padding-left: 22px;
    white-space: nowrap;
    letter-spacing: -0.3px;
  }
  .band--headline strong { font-weight: 700; margin-left: 10px; }
  .band--url {
    color: var(--link-blue);
    font-size: 32px;
    display: flex; align-items: center;
    padding-left: 23px;
    white-space: nowrap;
  }
  .sticker--top .band--headline { left: 190px; top: 0; width: 621px; height: 105px; border-radius: 0 4px 0 0; }
  .sticker--top .band--url { left: 190px; top: 105px; width: 621px; height: 101px; }
  .sticker--bottom .band--headline { left: 0; top: 0; width: 620px; height: 104px; border-radius: 70px 0 0 0; padding-left: 44px; }
  .sticker--bottom .band--url {
    left: 0; top: 104px; width: 620px; height: 101px; padding-left: 44px;
    background: linear-gradient(180deg, var(--note-yellow-top) 0%, var(--note-yellow-bottom) 100%);
  }

  .logo-panel {
    position: absolute; width: 190px;
    background: linear-gradient(180deg, #dedede 0%, var(--panel-white) 100%);
    box-shadow: 1px 0 3px rgba(0,0,0,0.12);
  }
  .sticker--top .logo-panel { left: 0; top: 0; height: 206px; border-radius: 60px 0 60px 0; }
  .sticker--bottom .logo-panel {
    left: 622px; top: 0; width: 189px; height: 205px; border-radius: 60px 4px 66px 0;
    background: linear-gradient(180deg, var(--panel-white) 0%, var(--panel-grey) 100%);
  }
  .logo {
    position: absolute; left: 18px; top: 76px;
    display: flex; align-items: flex-start; gap: 8px;
  }
  .logo__square { width: 30px; height: 28px; background: var(--logo-blue); margin-top: 18px; }
  .logo__name { font-size: 18px; color: var(--ink); white-space: nowrap; }
</style>
</head>
<body>
  <section class="sticker sticker--top" aria-label="Kanban sticker, logo left">
    <div class="sticker__base"></div>
    <div class="logo-panel">
      <div class="logo"><span class="logo__square"></span><span class="logo__name">quarveling ag</span></div>
    </div>
    <div class="band band--headline">Stop starting,<strong>Start finishing</strong></div>
    <div class="band band--url">www.quarveling.ch/kanban-coaching</div>
  </section>

  <section class="sticker sticker--bottom" aria-label="Kanban sticker, logo right">
    <div class="sticker__base"></div>
    <div class="band band--headline">Stop starting,<strong>Start finishing</strong></div>
    <div class="band band--url">www.quarveling.ch/kanban-coaching</div>
    <div class="logo-panel">
      <div class="logo"><span class="logo__square"></span><span class="logo__name">quarveling ag</span></div>
    </div>
  </section>
</body>
</html>
```